Branding website for a Data Science company with 1 product

Branding website for a Data Science company, featuring our main product: Quorlink. The purpose of the website is to get potential clients to get a peek at what we do, but the main purpose is to get them to get in touch with us. The website will not answer all questions. Therefore the contact details and contact form is a must-have .

Target Market(s)

Potential new B2B clients with medium to large websites, application users (behind a login)

Industry/Entity Type

It Company

Coding

Coded - Design and coding required

Number of Pages Required

2 page

Font styles to use
Sans Serif

Colors

Designer to choose colors to be used in the design.

Requirements
Must have
• A contact form and branding a product

```html
<!DOCTYPE html>
<html lang="en">
<head>
<meta charset="utf-8">
<title>Tallyform Associates — Data Science</title>
<link rel="stylesheet" href="https://fonts.googleapis.com/css2?family=Roboto:wght@400;500;700&family=Lato:wght@400;700&family=Montserrat:wght@500;600;700&display=swap">
<style>
  :root{
    --accent:#e23d16;
    --accent-dark:#b8290c;
    --ink:#2a2a2a;
    --muted:#6d6d6d;
    --light:#f6f6f6;
    --line:#e6c2b6;
    --field:#d9d9d9;
    --footer:#222222;
    --white:#ffffff;
  }
  *{box-sizing:border-box;margin:0;padding:0}
  html,body{width:1200px;height:3529px;overflow:hidden}
  body{position:relative;background:var(--white);font-family:'Lato',Arial,sans-serif;color:var(--ink)}
  .abs{position:absolute}

  /* Hero */
  .hero{left:0;top:0;width:1200px;height:576px;
    background:radial-gradient(circle at 30% 35%,#c9391f 0%,#8f1f10 45%,#5a120a 100%)}
  .hero-photo{position:absolute;inset:0;
    background:radial-gradient(circle at 75% 80%,rgba(230,170,160,.35) 0%,rgba(0,0,0,0) 35%),
               radial-gradient(circle at 12% 20%,rgba(240,120,90,.35) 0%,rgba(0,0,0,0) 30%)}
  .brand{left:100px;top:34px;display:flex;align-items:center;gap:12px;color:var(--white)}
  .brand-dot{width:44px;height:44px;border-radius:50%;border:2px solid var(--white)}
  .brand-name{font-family:'Roboto',Arial,sans-serif;font-weight:400;font-size:22px;letter-spacing:3px;line-height:1.05;text-transform:uppercase}
  .menu{right:98px;top:48px;color:var(--white);font-family:'Roboto',Arial,sans-serif;font-weight:700;font-size:16px;display:flex;align-items:center;gap:10px}
  .hero-title{left:0;top:260px;width:1200px;text-align:center;color:var(--white);
    font-family:'Roboto',Arial,sans-serif;font-weight:700;font-size:32px;line-height:58px;text-transform:uppercase;letter-spacing:.5px}
  .play{left:582px;top:370px}

  /* Welcome */
  .section-title{width:1200px;left:0;text-align:center;color:var(--accent);
    font-family:'Roboto',Arial,sans-serif;font-weight:700;font-size:29px;text-transform:uppercase}
  .section-sub{width:1200px;left:0;text-align:center;font-family:'Roboto',Arial,sans-serif;font-size:20px;color:#333}
  .intro{left:140px;width:920px;text-align:center;font-size:12.5px;line-height:22px;color:var(--muted)}
  .rule{left:150px;top:802px;width:900px;height:1px;background:var(--line)}

  .photo{background:linear-gradient(135deg,#1b2a48 0%,#3f6aa8 50%,#e88a2c 100%)}
  .h-accent{color:var(--accent);font-family:'Roboto',Arial,sans-serif;font-weight:700;text-transform:uppercase}
  .body-copy{font-size:12.5px;line-height:22px;color:var(--muted)}
  .btn-outline{display:flex;align-items:center;justify-content:center;gap:8px;border:2px solid var(--accent);color:var(--accent);
    font-family:'Roboto',Arial,sans-serif;font-weight:500;font-size:13px;text-transform:uppercase;width:142px;height:37px}

  /* Contact band */
  .band{left:0;top:1176px;width:1200px;height:542px;background:var(--light)}
  .help-title{left:134px;top:1245px;width:500px;font-family:'Roboto',Arial,sans-serif;font-weight:700;font-size:19px;line-height:38px;color:var(--accent)}
  .contact{left:682px;top:1219px;width:378px;height:468px;background:var(--white);border:1.5px solid #e7a68f}
  .contact h3{position:absolute;top:26px;width:100%;text-align:center;font-family:'Montserrat',Arial,sans-serif;font-weight:600;font-size:20px;color:#333;text-transform:uppercase}
  .contact p{position:absolute;top:70px;left:40px;width:298px;text-align:center;font-family:'Montserrat',Arial,sans-serif;font-weight:600;font-size:14px;line-height:22px;color:#222}
  .field{position:absolute;left:50px;width:286px;height:28px;border:1px solid var(--field);font-size:10.5px;color:#888;padding:6px 8px}
  .field.area{height:60px}
  .submit{position:absolute;left:66px;top:405px;width:252px;height:37px;background:var(--accent);color:var(--white);
    font-family:'Montserrat',Arial,sans-serif;font-weight:600;font-size:15px;display:flex;align-items:center;justify-content:center;text-transform:uppercase;letter-spacing:.5px}

  /* Services */
  .services-intro{left:140px;top:1810px;width:920px;text-align:center;font-size:12.5px;line-height:25px;color:var(--muted)}
  .svc-text{width:450px}
  .svc-text h4{font-family:'Roboto',Arial,sans-serif;font-weight:700;font-size:19px;color:var(--accent);text-transform:uppercase;margin-bottom:16px}
  .svc-text p{font-size:12.5px;line-height:24px;color:var(--muted);text-align:justify}
  .svc-img{width:498px;height:254px}

  /* Partners & footer */
  .partners{left:0;top:3247px;width:1200px;height:177px;background:var(--light);display:flex;align-items:center;justify-content:space-around;padding:0 70px}
  .partner{font-family:'Roboto',Arial,sans-serif;font-weight:500;font-size:30px;color:#333;display:flex;align-items:center;gap:10px}
  .partner-mark{width:26px;height:26px;border-radius:50%;background:#444}
  .footer{left:0;top:3424px;width:1200px;height:105px;background:var(--footer);color:var(--white)}
  .socials{position:absolute;top:23px;left:0;width:100%;display:flex;justify-content:center;gap:10px}
  .social{width:26px;height:26px;border-radius:50%;border:1.5px solid var(--white)}
  .copy{position:absolute;top:69px;width:100%;text-align:center;font-size:12px;font-weight:700}
  .page-no{position:absolute;right:22px;top:69px;font-size:11px}
</style>
</head>
<body>

<header class="abs hero" role="img" aria-label="Red toned photo of a glowing data network with connected nodes">
  <div class="hero-photo"></div>
</header>
<div class="abs brand">
  <span class="brand-dot"></span>
  <span class="brand-name">Tallyform<br>Associates</span>
</div>
<div class="abs menu">MENU
  <svg width="20" height="16" viewBox="0 0 20 16"><rect y="1" width="20" height="2.6" fill="#fff"/><rect y="7" width="20" height="2.6" fill="#fff"/><rect y="13" width="20" height="2.6" fill="#fff"/></svg>
</div>
<h1 class="abs hero-title">Identify your potential customers with the<br>help of data science</h1>
<svg class="abs play" width="36" height="36" viewBox="0 0 36 36"><circle cx="18" cy="18" r="17" fill="#fff"/><path d="M14 11 L25 18 L14 25Z" fill="var(--accent)"/></svg>

<h2 class="abs section-title" style="top:612px">Welcome to Tallyform Associates</h2>
<p class="abs section-sub" style="top:660px">Who are we &amp; what do we do</p>
<p class="abs intro" style="top:712px">We have a product called Quorlink. This is our on-demand, software-as-a-service to capture, learn and target our client's website visitors and turn them into loyal customers. Because of the easy and quick setup clients can in a record time start targeting their visitors instead of doing a large investment in new technology and data science. We help our clients to identify their potential customers with the help of data science. We therefore consider ourselves a data science company.</p>
<div class="abs rule"></div>

<div class="abs photo" style="left:134px;top:838px;width:454px;height:280px" role="img" aria-label="Photo of a hand touching a glowing digital screen"></div>
<h3 class="abs h-accent" style="left:621px;top:866px;font-size:19px">15+ Years of Experience</h3>
<p class="abs body-copy" style="left:621px;top:900px;width:450px">Lorem Ipsum is simply dummy text of the printing and typesetting industry. Lorem Ipsum has been the industry's standard dummy text ever since the 1500s, when an unknown printer took a galley of type and scrambled it to make a type specimen book. It has survived not only five centuries Lorem Ipsum is simply dummy text of the printing and typesetting industry. Lorem Ipsum has been the industry's standard dummy text ever since the 1500s, when an unknown.</p>
<div class="abs btn-outline" style="left:621px;top:1054px">Read more
  <svg width="16" height="8" viewBox="0 0 16 8"><path d="M0 4H14M10 1L14 4L10 7" stroke="currentColor" stroke-width="1.6" fill="none"/></svg>
</div>

<section class="abs band"></section>
<h3 class="abs help-title">We Help Our Clients To Identify Their Potential Customers With The Help Of Data Science</h3>
<div class="abs" style="left:134px;top:1327px;width:490px;height:179px;background:linear-gradient(135deg,#efe9e0 0%,#d8cfc2 60%,#b9ad9c 100%)" role="img" aria-label="Photo of a hand sketching a digital marketing diagram on paper"></div>
<p class="abs body-copy" style="left:134px;top:1522px;width:490px">Lorem Ipsum is simply dummy text of the printing and typesetting industry. Lorem Ipsum has been the industry's standard dummy text ever since the 1500s, when an unknown printer took a galley of type and scrambled it to make a type specimen book. It has survived not only five centuries Lorem Ipsum is simply dummy text of the printing and typesetting industry. Lorem Ipsum has been the industry's standard dummy.</p>
<div class="abs btn-outline" style="left:134px;top:1647px">Read more
  <svg width="16" height="8" viewBox="0 0 16 8"><path d="M0 4H14M10 1L14 4L10 7" stroke="currentColor" stroke-width="1.6" fill="none"/></svg>
</div>

<form class="abs contact">
  <h3>Contact us today</h3>
  <p>Complete this form to receive more information about program details &amp; more!</p>
  <div class="field" style="top:139px">First Name *</div>
  <div class="field" style="top:177px">Last Name *</div>
  <div class="field" style="top:216px">Phone *</div>
  <div class="field" style="top:256px">Email *</div>
  <div class="field" style="top:296px">Choose Our Service</div>
  <div class="field area" style="top:327px">Message</div>
  <div class="submit">Send me free info</div>
</form>

<h2 class="abs section-title" style="top:1754px">Our Core Services</h2>
<p class="abs services-intro">Lorem Ipsum is simply dummy text of the printing and typesetting industry. Lorem Ipsum has been the industry's standard dummy text ever since the 1500s, when an unknown printer took a galley of type and scrambled it to make a type specimen book. It has survived not only five centuries Lorem Ipsum is simply dummy text of the printing and typesetting industry. Lorem Ipsum has been the industry's standard dummy text ever since the 1500s, when an unknown printer took a galley of type and scrambled it to make a type specimen book. It has survived not only five centuries</p>

<!-- Advisory -->
<div class="abs svc-text" style="left:132px;top:1994px"><h4>Advisory</h4><p>Lorem Ipsum is simply dummy text of the printing and typesetting industry. Lorem Ipsum has been the industry's standard dummy text ever since the 1500s, when an unknown printer took a galley of type and scrambled it to make a type specimen book. It has survived not only five centuries Lorem Ipsum is simply dummy text of the printing and typesetting industry. Lorem Ipsum has been the industry's standard dummy.</p></div>
<div class="abs svc-img" style="left:593px;top:1946px;background:linear-gradient(180deg,#e9eef2 0%,#b7c2cc 55%,#5e6b77 100%)" role="img" aria-label="Photo of business people in silhouette talking at a window"></div>

<!-- Insights -->
<div class="abs svc-img" style="left:94px;top:2200px;background:radial-gradient(circle at 50% 50%,#2c3d5c 0%,#14203a 60%,#0b1222 100%)" role="img" aria-label="Illustration of a brain drawn as circuit lines"></div>
<div class="abs svc-text" style="left:650px;top:2248px"><h4>Insights</h4><p>Lorem Ipsum is simply dummy text of the printing and typesetting industry. Lorem Ipsum has been the industry's standard dummy text ever since the 1500s, when an unknown printer took a galley of type and scrambled it to make a type specimen book. It has survived not only five centuries Lorem Ipsum is simply dummy text of the printing and typesetting industry. Lorem Ipsum has been the industry's standard dummy.</p></div>

<!-- Targeting -->
<div class="abs svc-text" style="left:132px;top:2502px"><h4>Targeting &amp; Optimization</h4><p>Lorem Ipsum is simply dummy text of the printing and typesetting industry. Lorem Ipsum has been the industry's standard dummy text ever since the 1500s, when an unknown printer took a galley of type and scrambled it to make a type specimen book. It has survived not only five centuries Lorem Ipsum is simply dummy text of the printing and typesetting industry. Lorem Ipsum has been the industry's standard dummy.</p></div>
<div class="abs svc-img" style="left:597px;top:2454px;background:radial-gradient(circle at 45% 40%,#bfe0f5 0%,#3a7fb6 30%,#0f2c4d 70%,#071626 100%)" role="img" aria-label="Photo of a glowing globe surrounded by floating screens"></div>

<!-- Data engineering -->
<div class="abs svc-img" style="left:98px;top:2708px;background:linear-gradient(135deg,#dfe8ee 0%,#a9bccb 55%,#5b6e80 100%)" role="img" aria-label="Photo of a man working at a computer desk"></div>
<div class="abs svc-text" style="left:650px;top:2756px"><h4>Data Engineering</h4><p>Lorem Ipsum is simply dummy text of the printing and typesetting industry. Lorem Ipsum has been the industry's standard dummy text ever since the 1500s, when an unknown printer took a galley of type and scrambled it to make a type specimen book. It has survived not only five centuries Lorem Ipsum is simply dummy text of the printing and typesetting industry. Lorem Ipsum has been the industry's standard dummy.</p></div>

<!-- Privacy -->
<div class="abs svc-text" style="left:132px;top:3010px"><h4>Data Privacy and Security</h4><p>Lorem Ipsum is simply dummy text of the printing and typesetting industry. Lorem Ipsum has been the industry's standard dummy text ever since the 1500s, when an unknown printer took a galley of type and scrambled it to make a type specimen book. It has survived not only five centuries Lorem Ipsum is simply dummy text of the printing and typesetting industry. Lorem Ipsum has been the industry's standard dummy.</p></div>
<div class="abs svc-img" style="left:597px;top:2962px;background:radial-gradient(circle at 45% 45%,#7ecbf0 0%,#2a78b0 35%,#0c2a48 75%,#061523 100%)" role="img" aria-label="Illustration of an open blue padlock over digital code"></div>

<section class="abs partners">
  <span class="partner"><span class="partner-mark"></span>Loanmark</span>
  <span class="partner">Vesk Lab</span>
  <span class="partner">Orbitra</span>
  <span class="partner"><span class="partner-mark"></span>Mixwell</span>
</section>

<footer class="abs footer">
  <div class="socials">
    <span class="social"></span><span class="social"></span><span class="social"></span><span class="social"></span><span class="social"></span><span class="social"></span>
  </div>
  <p class="copy">© Copyright 2017 Tallyform Associates. All Rights Reserved. Privacy Policy.</p>
  <span class="page-no">C12</span>
</footer>

</body>
</html>
```